Maple Grove Schools | brand new stationery!

We need stationery design with our new logo! Our company updated it's name and image and we like to incorporate the new one on our stationery, business cards and email signature. We are looking for fresh, new ideas!
Industry: Childcare, Elementary and Middle School
Company Name: Maple Grove Schools
Tagline: Bright Futures Start Here
Main colors: Blue, white and a little yellow
Star shape is something new for us! Do you see a way to incorporate it as a design element?

```html
<!DOCTYPE html>
<html lang="en">
<head>
<meta charset="utf-8">
<title>Maple Grove Schools – Business Card</title>
<link href="https://fonts.googleapis.com/css2?family=Josefin+Sans:wght@600&family=Poppins:wght@600&family=Roboto:wght@400&display=swap" rel="stylesheet">
<style>
  :root {
    --page-bg: #e9e6e1;
    --navy-deep: #0b0f45;
    --navy-mid: #1d2466;
    --navy-soft: #2b3373;
    --frost: #d9dadf;
    --frost-edge: #f2f2f4;
    --gold: #e8a21f;
    --white: #ffffff;
    --ink: #111325;
  }
  * { margin: 0; padding: 0; box-sizing: border-box; }
  html, body { width: 1200px; height: 969px; overflow: hidden; }
  body { background: var(--page-bg); position: relative; }

  .business-card {
    position: absolute;
    left: 167px; top: 238px;
    width: 866px; height: 492px;
    border-radius: 22px;
    overflow: hidden;
    background: radial-gradient(ellipse at 35% 60%, var(--navy-soft) 0%, var(--navy-mid) 40%, var(--navy-deep) 80%);
    box-shadow: 0 14px 40px rgba(0,0,0,0.22);
  }
  .card-shapes { position: absolute; inset: 0; }
  .edge-tab {
    position: absolute; left: 0; top: 117px;
    width: 12px; height: 58px;
    background: var(--frost-edge);
    border-radius: 0 4px 4px 0;
  }
  .holder { position: absolute; left: 57px; top: 116px; color: var(--white); }
  .holder-name {
    font-family: "Josefin Sans", sans-serif; font-weight: 600;
    font-size: 35px; letter-spacing: 1.5px; line-height: 1;
  }
  .holder-title {
    font-family: "Roboto", sans-serif; font-size: 19px;
    color: var(--gold); margin-top: 8px;
  }
  .contact-list {
    position: absolute; left: 59px; top: 198px;
    list-style: none; color: var(--white);
    font-family: "Roboto", sans-serif; font-size: 19px; line-height: 24px;
  }
  .contact-list li { display: flex; align-items: flex-start; }
  .contact-list li.address { margin-bottom: 11px; }
  .contact-icon { width: 16px; height: 16px; margin: 4px 14px 0 0; flex: none; }
  .contact-icon svg { width: 16px; height: 16px; display: block; fill: var(--gold); }

  .brand-name {
    position: absolute; left: 520px; top: 232px; width: 300px;
    text-align: center;
    font-family: "Poppins", sans-serif; font-weight: 600;
    font-size: 44px; line-height: 1.05; color: var(--ink);
    display: flex; flex-direction: column; align-items: center;
  }
  .brand-dot {
    width: 22px; height: 22px; border-radius: 50%;
    background: var(--navy-deep); margin-bottom: 14px;
  }
</style>
</head>
<body>
  <div class="business-card">
    <svg class="card-shapes" width="866" height="492" viewBox="0 0 866 492">
      <defs>
        <linearGradient id="frostFill" x1="0" y1="0" x2="1" y2="1">
          <stop offset="0" stop-color="#cfd0d8"/>
          <stop offset="0.5" stop-color="#e3e3e6"/>
          <stop offset="1" stop-color="#c9cad2"/>
        </linearGradient>
      </defs>
      <path class="frost-panel" d="M620 0 H866 V492 H560 C520 420 470 360 470 300 C470 250 520 230 540 200 C560 160 560 80 620 0 Z" fill="url(#frostFill)" opacity="0.92"/>
      <path class="frost-rim" d="M620 0 C560 80 560 160 540 200 C520 230 470 250 470 300 C470 360 520 420 560 492" fill="none" stroke="#f4f4f6" stroke-width="10" opacity="0.8"/>
    </svg>

    <div class="edge-tab"></div>

    <div class="holder">
      <div class="holder-name">DANIEL REYES</div>
      <div class="holder-title">President</div>
    </div>

    <ul class="contact-list">
      <li class="address">
        <span class="contact-icon"><svg viewBox="0 0 16 16"><path d="M8 0a5.5 5.5 0 0 0-5.5 5.5C2.5 10 8 16 8 16s5.5-6 5.5-10.5A5.5 5.5 0 0 0 8 0zm0 8a2.5 2.5 0 1 1 0-5 2.5 2.5 0 0 1 0 5z"/></svg></span>
        <span>4120 Birchwood Avenue<br>Fairview, Oregon 97024</span>
      </li>
      <li>
        <span class="contact-icon"><svg viewBox="0 0 16 16"><path d="M3.6 1 6 3.8 4.7 5.6a9 9 0 0 0 5.7 5.7l1.8-1.3L15 12.4 13.4 15C6.6 15 1 9.4 1 2.6z"/></svg></span>
        <span>555-214-7730</span>
      </li>
      <li>
        <span class="contact-icon"><svg viewBox="0 0 16 16"><path d="M4 0h8a1 1 0 0 1 1 1v14a1 1 0 0 1-1 1H4a1 1 0 0 1-1-1V1a1 1 0 0 1 1-1zm.8 1.6v11h6.4v-11z"/></svg></span>
        <span>555-618-2045</span>
      </li>
      <li>
        <span class="contact-icon"><svg viewBox="0 0 16 16"><path d="M4 1h8v4H4zM1 6h14v6h-2v-2H3v2H1zm3 5h8v4H4z"/></svg></span>
        <span>555-309-4182</span>
      </li>
      <li>
        <span class="contact-icon"><svg viewBox="0 0 16 16"><path d="M1 4h14v9H1zm1.2 1L8 9l5.8-4z"/></svg></span>
        <span>info@maplegroveschools.com</span>
      </li>
      <li>
        <span class="contact-icon"><svg viewBox="0 0 16 16"><path d="M8 1a7 7 0 1 0 0 14A7 7 0 0 0 8 1zm-1 2.2L5.5 5 6 7.5 4 9 3 6.3A5.5 5.5 0 0 1 7 3.2zm2.5 10.3L9 11l2-2 2 1.3a5.5 5.5 0 0 1-3.5 3.2z"/></svg></span>
        <span>maplegroveschools.com</span>
      </li>
    </ul>

    <div class="brand-name">
      <span class="brand-dot"></span>
      <span>Maple Grove</span>
      <span>Schools</span>
    </div>
  </div>
</body>
</html>
```